Wordpress Design Project

Hi- We are seeking a Wordpress Theme Design that will best serve as an introduction of our company, Kestrel Trading Co, to potential international clients on the web.

We are a relationship management company that help build connections between professional music equipment manufacturers and high-volume professional music equipment users, i.e concert venue managers, equipment resellers, club owners, djs,etc.

We would like to see designs to incorporate the following:

- If possible a music theme tastefully designed into the company name/logo on the wordpress home page (not a dealbreaker without)

-We are choosing the Wordpress CMS because we're looking for the site to be more centered around our blog, which will be the main medium where we connect with clients and potential clients, where these previously strangers that we meet briefly on our travelings can get to know us better by coming to the site. The relationship, and the rapport that they feel towards my team and I, will be the key driver in determining whether they will want to do business through us or not. The products are secondary in importance. It is after the visitor feel comfortable doing business through us that they will venture to check out the products that we offer. Finally, the website is not a sales point, there will not be a feature for someone to buy something from the site.

Long story short, this website is meant to be a communications channel and not a sales channel.

-Need a contacts form application built-in to capture interested client information to facilitate the off-site sales process.

- Would prefer the theme to give a minimalist and conservative feel, and ideally capture the concept of our globalized world and the synergizing role that music plays in bringing people together.

-Ideally the design should incorporate subtle references to the Generation Y values that inspired our company name and mission:

-Emphasis on partnership and teamwork
-Belief and aspiration for win/win trade relations
-Fast, honest, and transparent service
-Make the world a better place via trade

Theme example (function-wise): http://demo2.lumaframes.com/?name=brsk

Product Type examplex: http://www.qorv.com.cn/en/product.asp

(Willing to pay extra if the winning design can be coded to full functionality)
Updates

To all those designers who've accepted the contest invitation, can you please send me a quick message to confirm if you are still planning on submitting by the end of the day tomorrow, 8/9. Otherwise we will make a selection ahead of the deadline so we can speed up our website live date. Thanks!

Target Market(s)

High volume/frequency professional music equipment users/resellers. Concert venues, DJs, Dance Clubs, etc

Industry/Entity Type

Communications

Requirements
Must have
• Blog
Product Showcase Page that is easy to update and expand.
About Page
Contact Forms Application built-in
Nice to have
• Music theme designed into company name/logo

```html
<!DOCTYPE html>
<html lang="en">
<head>
<meta charset="utf-8">
<title>Kestrel Trading Co</title>
<link rel="stylesheet" href="https://fonts.googleapis.com/css2?family=Ubuntu:wght@400;500&family=Source+Sans+3:ital,wght@0,400;0,600;1,400&family=PT+Serif:wght@700&display=swap">
<style>
:root{
  --bg:#cfd3de;
  --page:#ffffff;
  --navy:#1f2a6b;
  --ink:#2a3580;
  --text:#2d3566;
  --band:#e6ecf5;
  --line:#c8cfe0;
  --soft:#eef1f7;
  --rule:#2a3a99;
}
*{box-sizing:border-box;margin:0;padding:0}
html,body{width:714px;height:1200px;overflow:hidden}
body{background:var(--bg);font-family:"Source Sans 3",Arial,sans-serif;color:var(--text);position:relative}
.page{position:absolute;left:40px;top:0;width:634px;height:1152px;background:var(--page);border-top:3px solid var(--navy)}
.abs{position:absolute}

/* header */
.header{left:0;top:0;width:634px;height:70px;background:linear-gradient(#fff,#f1f2f6)}
.brand{left:20px;top:24px;display:flex;align-items:center;gap:6px;font-family:"Ubuntu",sans-serif;font-size:18px;color:var(--navy)}
.brand-mark{width:16px;height:16px;background:var(--navy);border-radius:50%}
.nav{right:20px;top:36px;display:flex;gap:0;font-family:"Ubuntu",sans-serif;font-size:10px}
.nav a{color:var(--ink);text-decoration:none;padding:4px 10px;line-height:10px;border-radius:3px}
.nav a.active{background:var(--navy);color:#fff;padding:4px 12px}

/* hero */
.hero{left:0;top:70px;width:634px;height:208px;background:linear-gradient(160deg,#3a4aa8 0%,#22307a 35%,#4b4f7a 60%,#1c2150 100%)}
.hero-dots{left:270px;top:194px;width:64px;height:14px;background:#fff;border-radius:10px 10px 0 0;display:flex;justify-content:center;align-items:center;gap:4px}
.hero-dots span{width:5px;height:5px;border-radius:50%;background:#9aa2c0}
.hero-dots span:first-child{background:var(--navy)}

/* welcome */
.welcome{left:15px;top:297px;width:600px}
.section-title{font-family:"Ubuntu",sans-serif;font-size:13px;color:var(--ink);font-weight:400}
.section-title b{color:var(--navy);font-weight:500}
.welcome p{font-size:7px;line-height:11px;color:var(--ink);margin-top:9px}
.divider{left:0;width:634px;height:1px;background:#e3e6ee}

/* products */
.products-title{left:14px;top:420px}
.grid{left:12px;top:442px;width:608px;display:grid;grid-template-columns:repeat(4,152px)}
.row{border:1px solid var(--line)}
.cell{height:117px;border-right:1px solid var(--line);position:relative;background:#fff}
.cell:nth-child(4n){border-right:none}
.cell .shot{position:absolute;left:20px;top:30px;width:110px;height:34px;background:linear-gradient(#5a5f6a,#23262d);border-radius:2px}
.cell .shot.tall{left:54px;top:5px;width:42px;height:78px;background:linear-gradient(#2a2d33,#0f1013)}
.cell .shot.green{background:linear-gradient(#3d5a48,#1d2c22)}
.cell .caption{position:absolute;left:0;bottom:0;width:100%;height:25px;background:var(--band);font-size:9px;color:var(--ink);line-height:25px;padding-left:9px}

/* lower box */
.lower{left:10px;top:717px;width:614px;height:413px;border:1px solid var(--line)}
.blog{left:0;top:0;width:429px;height:411px}
.blog-head{left:0;top:0;width:429px;height:34px;border-bottom:1px solid var(--line)}
.blog-head .section-title{position:absolute;left:14px;top:11px}
.post{left:9px;width:410px;height:110px}
.post .thumb{position:absolute;left:0;top:0;width:126px;height:101px;border:2px solid #e2e4ea}
.post .body{position:absolute;left:135px;top:8px;width:270px}
.post h3{font-family:"Source Sans 3",sans-serif;font-weight:400;font-size:11px;color:#1d2250}
.post p{font-size:7px;line-height:12px;color:var(--ink);margin-top:4px}
.post .more{font-size:7.5px;color:#1d2250;margin-top:2px;display:flex;align-items:center;gap:4px}
.post .meta{display:inline-block;margin-top:5px;background:var(--soft);padding:3px 6px;font-size:9px;color:var(--ink)}
.post .meta small{font-size:7px}

.sidebar{left:429px;top:0;width:183px;height:411px;border-left:1px solid var(--line);background:var(--soft)}
.contact{left:0;top:0;width:183px;height:249px;background:#fff}
.contact .section-title{position:absolute;left:11px;top:12px}
.contact .bar{position:absolute;left:0;top:32px;width:183px;height:2px;background:var(--rule)}
.field{position:absolute;left:10px;width:164px;height:19px;border:1px solid var(--line);background:#fff;font-size:7.5px;color:var(--ink);padding:4px 6px;font-family:inherit}
.btn{position:absolute;top:215px;height:18px;font-size:9px;border-radius:3px;line-height:16px;text-align:center}
.btn.submit{left:12px;width:58px;background:var(--navy);color:#fff;border:1px solid var(--navy)}
.btn.reset{left:75px;width:52px;background:var(--band);color:var(--ink);border:1px solid #aab3cc}
.testi-head{left:0;top:252px;width:183px;height:30px;background:#fff}
.testi-head .section-title{position:absolute;left:11px;top:10px}
.testi-head .bar{position:absolute;left:0;top:30px;width:183px;height:2px;background:var(--rule)}
.testi{left:11px;top:294px;width:166px;font-size:7px;line-height:12px;font-style:italic;color:var(--ink)}
.testi .face{float:left;width:50px;height:45px;margin:0 6px 0 0;background:linear-gradient(#7a6a55,#3a342c)}
.testi .lead{font-size:9px}
.testi .author{font-family:"PT Serif",serif;font-style:normal;font-weight:700;font-size:8.5px;color:var(--navy);margin-top:2px}

.footer{left:42px;top:1167px;font-size:7px;color:var(--ink)}
</style>
</head>
<body>
<div class="page">
  <header class="header abs">
    <div class="brand abs"><span class="brand-mark"></span><span>Kestrel Trading Co</span></div>
    <nav class="nav abs">
      <a class="active">Home</a><a>About Us</a><a>Blog</a><a>Products</a><a>Testimonials</a><a>Services</a><a>Contact</a>
    </nav>
  </header>

  <section class="hero abs" role="img" aria-label="Recording studio with mixing console and monitor speakers">
    <div class="hero-dots abs"><span></span><span></span><span></span><span></span><span></span></div>
  </section>

  <section class="welcome abs">
    <h2 class="section-title">Welcome to <b>Kestrel Trading Co</b></h2>
    <p>Brightlane eSolutions is a web service company, offering a wide range of services which range from designing and development, that is covering almost all the fields in the best possible way.<br>To be the best we know what and how to present beautifully the working of the client's need and their advantages be highlighted. We act in accordance with the Industry certified processes to<br>deliver the best to our clients all over the world.</p>
    <p>Thus, Wanna get ahead in the competition with other website. Brightlane esolutions provide you with an attractive and most convincing website to enhance your marketing goals.<br>The only way to success is through the right path and that's what we provide you. None of the other companies has the result we do.</p>
  </section>
  <div class="divider abs" style="top:406px"></div>

  <h2 class="section-title products-title abs">Featured <b>Products</b></h2>
  <div class="grid abs row" style="top:442px">
    <div class="cell"><div class="shot" role="img" aria-label="Power amplifier"></div><div class="caption">Model XM-300 | LEARN MORE</div></div>
    <div class="cell"><div class="shot" role="img" aria-label="Power amplifier"></div><div class="caption">Model XM-300 | LEARN MORE</div></div>
    <div class="cell"><div class="shot" role="img" aria-label="Power amplifier"></div><div class="caption">Model XM-300 | LEARN MORE</div></div>
    <div class="cell"><div class="shot" role="img" aria-label="Power amplifier"></div><div class="caption">Model XM-300 | LEARN MORE</div></div>
  </div>
  <div class="grid abs row" style="top:567px">
    <div class="cell"><div class="shot" role="img" aria-label="Power amplifier"></div><div class="caption">Model XM-300 | LEARN MORE</div></div>
    <div class="cell"><div class="shot" role="img" aria-label="Power amplifier"></div><div class="caption">Model XM-300 | LEARN MORE</div></div>
    <div class="cell"><div class="shot tall" role="img" aria-label="Loudspeaker cabinet"></div><div class="caption">Model XM-300 | LEARN MORE</div></div>
    <div class="cell"><div class="shot green" role="img" aria-label="Signal processor"></div><div class="caption">Model XM-300 | LEARN MORE</div></div>
  </div>
  <div class="divider abs" style="top:703px"></div>

  <section class="lower abs">
    <div class="blog abs">
      <div class="blog-head abs"><h2 class="section-title">Recent <b>Blog</b></h2></div>

      <article class="post abs" style="top:45px">
        <div class="thumb" role="img" aria-label="Home studio with mixing desk and monitors" style="background:linear-gradient(135deg,#c07a3a,#5a3a22 60%,#2a2a30)"></div>
        <div class="body">
          <h3>Vel ut quas utroque placerat, kasd utinam epicuri at</h3>
          <p>est, hendrerit argumentum dissentias ei nec. Vel ut quas utroque placerat, kasd utinam epicuri at est, hendrerit argumentum dissentias ei nec. Vel ut quas utroque placerat, kasd utinam epicuri at est, hendrerit argumentum dissentias ei nec. Vel ut quas utroque placerat, kasd utinam epicuri at est,</p>
          <div class="more">CONTINUE READING <svg width="5" height="7" viewBox="0 0 5 7"><path d="M1 1l2.5 2.5L1 6" fill="none" stroke="#1d2250"/></svg></div>
          <div class="meta"><small>Posted on</small> 04/02/2012 &nbsp;| 252 Comments</div>
        </div>
      </article>

      <article class="post abs" style="top:166px">
        <div class="thumb" role="img" aria-label="Black and white studio workstation" style="background:linear-gradient(135deg,#d8d8d8,#6a6a6a 55%,#222)"></div>
        <div class="body">
          <h3>kasd utinam epicuri</h3>
          <p>est, hendrerit argumentum dissentias ei nec. Vel ut quas utroque placerat, kasd utinam epicuri at est, hendrerit argumentum dissentias ei nec. Vel ut quas utroque placerat, kasd utinam epicuri at est, hendrerit argumentum dissentias ei nec. Vel ut quas utroque placerat, kasd utinam epicuri at est,</p>
          <div class="more">CONTINUE READING <svg width="5" height="7" viewBox="0 0 5 7"><path d="M1 1l2.5 2.5L1 6" fill="none" stroke="#1d2250"/></svg></div>
          <div class="meta"><small>Posted on</small> 04/02/2012 &nbsp;| 252 Comments</div>
        </div>
      </article>

      <article class="post abs" style="top:289px">
        <div class="thumb" role="img" aria-label="Sound engineer beside a rack of outboard gear" style="background:linear-gradient(135deg,#8a7260,#3a3a3a 55%,#1a1a1a)"></div>
        <div class="body">
          <h3>Pellentesque habitant morbi tristique senectus</h3>
          <p>est, hendrerit argumentum dissentias ei nec. Vel ut quas utroque placerat, kasd utinam epicuri at est, hendrerit argumentum dissentias ei nec. Vel ut quas utroque placerat, kasd utinam epicuri at est, hendrerit argumentum dissentias ei nec. Vel ut quas utroque placerat, kasd utinam epicuri at est,</p>
          <div class="more">CONTINUE READING <svg width="5" height="7" viewBox="0 0 5 7"><path d="M1 1l2.5 2.5L1 6" fill="none" stroke="#1d2250"/></svg></div>
          <div class="meta"><small>Posted on</small> 04/02/2012 &nbsp;| 252 Comments</div>
        </div>
      </article>
    </div>

    <aside class="sidebar abs">
      <form class="contact abs">
        <h2 class="section-title">Quick Contact Form</h2>
        <div class="bar"></div>
        <div class="field" style="top:42px">type your name</div>
        <div class="field" style="top:70px">type your email address</div>
        <div class="field" style="top:99px">type your phone no.</div>
        <div class="field" style="top:128px;height:80px">query/message</div>
        <div class="btn submit">Submit Now</div>
        <div class="btn reset">Reset Now</div>
      </form>
      <div class="testi-head abs"><h2 class="section-title">Testimonials</h2><div class="bar"></div></div>
      <div class="testi abs">
        <div class="face" role="img" aria-label="Client portrait"></div>
        <span class="lead">Tittle line goes here</span> advanced web projects and the ongoing projects that require permanent maintenance and support We like challenges and do complete these challenge with expertise We at Brightlane provide you the best simple websites too with total work done as using
        <div class="author">By Author Name</div>
      </div>
    </aside>
  </section>
</div>
<footer class="footer abs">© 2012 Company Name &nbsp;| &nbsp;All right reserved &nbsp;| &nbsp;Term &amp; Conditions</footer>
</body>
</html>
```